Capacity building in Resource Management

Need design of a business card (later to be completed by letterhead and webdesign in same fashion) for a professional who works in the field of capacity building of professionals in mostly developing countries in the field waste/resource management, waste prevention/reduction, cleaner production, stakeholders involvement, etc.
Info on business cards is to include provided logo, info in provided file and picture.

Industry/Entity Type

Business

Contact Information for Business Card

White background

Font styles to use
Sans Serif

Colors

Designer to choose colors to be used in the design.

```html
<!DOCTYPE html>
<html lang="en">
<head>
<meta charset="utf-8">
<title>Terra-Skola Business Card</title>
<link href="https://fonts.googleapis.com/css2?family=Roboto:wght@400;500;700&display=swap" rel="stylesheet">
<style>
  :root {
    --backdrop: #e9e7e3;
    --card-white: #ffffff;
    --green-brand: #3e8a2c;
    --green-tab: #5c9f3f;
    --green-tab-light: #6fae4e;
    --green-band: #3f7a2a;
    --green-band-light: #5a9142;
    --photo-frame: #3e7a2c;
    --photo-top: #8fae86;
    --photo-bottom: #c9c6bd;
    --text-light: #ffffff;
  }
  * { box-sizing: border-box; margin: 0; padding: 0; }
  html, body {
    width: 1200px; height: 1047px; overflow: hidden;
    background: var(--backdrop);
    font-family: "Roboto", Arial, sans-serif;
  }
  .card {
    position: absolute; left: 100px; top: 250px;
    width: 1000px; height: 546px;
    background: var(--card-white);
    border-radius: 26px; overflow: hidden;
    box-shadow: 0 12px 34px rgba(0,0,0,0.18);
  }
  .brand {
    position: absolute; left: 60px; top: 78px;
    display: flex; align-items: center; gap: 18px;
  }
  .brand-mark {
    width: 54px; height: 54px; border-radius: 50%;
    background: var(--green-brand);
  }
  .brand-name {
    font-size: 62px; font-weight: 700; color: var(--green-brand);
    letter-spacing: 0.5px; line-height: 1;
  }
  .portrait {
    position: absolute; left: 709px; top: 57px;
    width: 236px; height: 254px;
    border: 4px solid var(--photo-frame);
    background: linear-gradient(160deg, var(--photo-top), var(--photo-bottom));
  }
  .title-tab { position: absolute; left: 0; top: 240px; width: 450px; height: 112px; }
  .title-text { position: absolute; left: 52px; top: 244px; color: var(--text-light); }
  .title-text h1 { font-size: 37px; font-weight: 500; line-height: 42px; }
  .title-text p { font-size: 22px; font-weight: 400; line-height: 29px; margin-top: 0; }
  .contact-band {
    position: absolute; left: 0; top: 351px; width: 1000px; height: 195px;
    background: linear-gradient(100deg, var(--green-band) 0%, var(--green-band-light) 45%, var(--green-band) 80%);
  }
  .contact-list {
    position: absolute; left: 52px; top: 40px; list-style: none;
    color: var(--text-light); font-size: 23px;
  }
  .contact-list li { display: flex; align-items: center; height: 30px; gap: 16px; }
  .contact-list svg { width: 18px; height: 18px; flex: none; }
  .social-list {
    position: absolute; right: 52px; top: 70px; list-style: none;
    color: var(--text-light); font-size: 23px; text-align: right;
  }
  .social-list li { display: flex; align-items: center; justify-content: flex-end; height: 30px; gap: 18px; }
  .social-dot { width: 14px; height: 14px; border-radius: 50%; background: var(--text-light); flex: none; }
</style>
</head>
<body>
  <div class="card">
    <div class="brand">
      <span class="brand-mark"></span>
      <span class="brand-name">terra-skola</span>
    </div>

    <div class="portrait" role="img" aria-label="Portrait photo of Jorik Veldman outdoors"></div>

    <svg class="title-tab" viewBox="0 0 450 112" aria-hidden="true">
      <defs>
        <linearGradient id="tabGrad" x1="0" y1="0" x2="1" y2="0">
          <stop offset="0" stop-color="#5c9f3f"/>
          <stop offset="1" stop-color="#6fae4e"/>
        </linearGradient>
      </defs>
      <polygon points="0,0 366,0 446,112 0,112" fill="url(#tabGrad)"/>
    </svg>
    <div class="title-text">
      <h1>Terra-Skola</h1>
      <p>Capacity building in<br>Resource Management</p>
    </div>

    <div class="contact-band">
      <ul class="contact-list">
        <li>
          <svg viewBox="0 0 18 18"><path d="M4 2l3 1 1 4-2 1.5c1 2 2.5 3.5 4.5 4.5L12 11l4 1 1 3-2 2C8 16 2 10 1.5 4z" fill="#fff"/></svg>
          +49 1500 412 7738 (also whatsap)
        </li>
        <li>
          <svg viewBox="0 0 18 18"><rect x="2" y="4" width="14" height="10" fill="none" stroke="#fff" stroke-width="1.6"/><path d="M2 4l7 6 7-6" fill="none" stroke="#fff" stroke-width="1.6"/></svg>
          jorik.veldman@terra-skola.com
        </li>
        <li>
          <svg viewBox="0 0 18 18"><circle cx="9" cy="9" r="7" fill="none" stroke="#fff" stroke-width="1.4"/><ellipse cx="9" cy="9" rx="3" ry="7" fill="none" stroke="#fff" stroke-width="1.2"/><path d="M2 9h14M3.5 5.5h11M3.5 12.5h11" stroke="#fff" stroke-width="1.1"/></svg>
          www.terra-skola.com
        </li>
        <li>
          <svg viewBox="0 0 18 18"><path d="M1 9L9 2l8 7h-2.5v7h-4v-4.5h-3V16h-4V9z" fill="#fff"/></svg>
          Lindenweg 12 10115 Berlin Germany
        </li>
      </ul>
      <ul class="social-list">
        <li>@jorikveldman <span class="social-dot"></span></li>
        <li>veld2004 <span class="social-dot"></span></li>
        <li>Jorik Veldman <span class="social-dot"></span></li>
      </ul>
    </div>
  </div>
</body>
</html>
```